Wedding Decor and Entertianment business card

Company - We run a weddings and events company called Amber Fern, we provide most entertainment and decor services to our customers.

Initial idea is ....
A simple business card with logo on the front, this will be spot varnish. On a matt black background.
The reverse will be simple contact information.

But happy to try things outside of the box and would welcome some crazy ideas.

Target Market(s)

wedding couples - 21 - 40
High end wedding venues.

Industry/Entity Type

Wedding

Contact Information for Business Card

01742 918 263
amberfern.co.uk
rupert@amberfern.co.uk
or
eleanor@amberfern.co.uk

Requirements
Nice to have
• black matt background with spot varnish logo on the front.

```html
<!DOCTYPE html>
<html lang="en">
<head>
<meta charset="utf-8">
<title>Amber Fern – Business Card</title>
<link rel="stylesheet" href="https://fonts.googleapis.com/css2?family=Jost:wght@400&family=Open+Sans:wght@400&display=swap">
<style>
  :root {
    --backdrop: #e8c5c1;
    --matt-black: #0d0d0d;
    --varnish: #2b2d31;
    --plum: #7d547c;
    --plum-text: #8e5d8f;
    --ink: #111111;
    --paper: #ffffff;
    --divider: #3a3a3a;
    --icon: #5a5a5a;
  }
  * { margin: 0; padding: 0; box-sizing: border-box; }
  html, body { width: 1200px; height: 900px; overflow: hidden; }
  body { background: var(--backdrop); position: relative; font-family: "Open Sans", sans-serif; }

  .card { position: absolute; width: 560px; height: 320px; box-shadow: 0 6px 14px rgba(0,0,0,0.25); overflow: hidden; }

  /* Front */
  .card--front { left: 70px; top: 90px; background: var(--matt-black); display: flex; align-items: center; justify-content: center; gap: 18px; }
  .front-mark { width: 46px; height: 46px; border-radius: 50%; border: 6px solid var(--varnish); }
  .front-name { font-family: "Jost", sans-serif; font-size: 40px; letter-spacing: 8px; color: var(--varnish); text-transform: uppercase; }

  /* Back */
  .card--back { left: 570px; top: 440px; background: var(--paper); }
  .band-top { position: absolute; left: 0; top: 0; width: 100%; height: 12px; background: var(--plum); }
  .band-bottom { position: absolute; left: 0; bottom: 0; width: 100%; height: 20px; background: var(--plum); }

  .brand { position: absolute; top: 52px; left: 0; width: 100%; display: flex; align-items: center; justify-content: center; gap: 16px; }
  .brand-mark { width: 30px; height: 30px; border-radius: 50%; border: 4px solid var(--ink); }
  .brand-name { font-family: "Jost", sans-serif; font-size: 28px; letter-spacing: 9px; color: var(--ink); text-transform: uppercase; }

  .contact-band { position: absolute; left: 0; top: 140px; width: 100%; height: 114px; background: var(--matt-black); display: flex; align-items: center; }
  .person-name { width: 270px; padding-left: 72px; font-size: 27px; color: var(--plum-text); text-transform: uppercase; letter-spacing: -0.5px; }
  .divider { width: 2px; height: 82px; background: var(--divider); }
  .contact-list { list-style: none; padding-left: 20px; }
  .contact-list li { display: flex; align-items: center; gap: 12px; font-size: 15px; line-height: 20px; color: var(--plum-text); }
  .contact-list svg { width: 14px; height: 14px; fill: none; stroke: var(--icon); stroke-width: 1.6; }
</style>
</head>
<body>

  <section class="card card--front" aria-label="Card front">
    <span class="front-mark" aria-hidden="true"></span>
    <span class="front-name">Amber Fern</span>
  </section>

  <section class="card card--back" aria-label="Card back">
    <div class="band-top"></div>

    <div class="brand">
      <span class="brand-mark" aria-hidden="true"></span>
      <span class="brand-name">Amber Fern</span>
    </div>

    <div class="contact-band">
      <p class="person-name">Oliver Hart</p>
      <span class="divider"></span>
      <ul class="contact-list">
        <li>
          <svg viewBox="0 0 16 16" aria-hidden="true"><path d="M3 2h3l1.5 3.5-2 1.2a8 8 0 0 0 3.8 3.8l1.2-2L14 10v3a1 1 0 0 1-1 1A11 11 0 0 1 2 3a1 1 0 0 1 1-1z"/></svg>
          01742 918 263
        </li>
        <li>
          <svg viewBox="0 0 16 16" aria-hidden="true"><circle cx="8" cy="8" r="6.5"/><ellipse cx="8" cy="8" rx="2.8" ry="6.5"/><path d="M1.5 8h13"/></svg>
          amberfern.co.uk
        </li>
        <li>
          <svg viewBox="0 0 16 16" aria-hidden="true"><rect x="1.5" y="3.5" width="13" height="9"/><path d="M1.5 3.5 8 9l6.5-5.5"/></svg>
          rupert@amberfern.co.uk
        </li>
      </ul>
    </div>

    <div class="band-bottom"></div>
  </section>

</body>
</html>
```